Web Design Project

we require new design / layout for www.brimlodge.eu design clean easy read must send strong and industrial theme as selling point to our product is the strength in our products

To include step process for the www.brimlodge.eu/designer2

For step process have similar layout to http://www.thewaxgarden.com/create/own_temp.php

Industry/Entity Type

Industrial

```html
<!DOCTYPE html>
<html lang="en">
<head>
<meta charset="utf-8">
<title>Brimlodge – Pop Up Gazebos</title>
<link href="https://fonts.googleapis.com/css2?family=Ubuntu:wght@300;400;500&display=swap" rel="stylesheet">
<style>
:root{
  --navy:#1a3a8c;
  --navy-dark:#0f2a6e;
  --red:#d5141b;
  --text:#3a4a6a;
  --muted:#7a8090;
  --line:#e2e4ea;
  --panel:#f1f2f4;
  --footer:#f6f6f7;
  --bottom:#ececee;
}
*{margin:0;padding:0;box-sizing:border-box}
html,body{width:778px;height:1200px;overflow:hidden;background:#fff}
body{position:relative;font-family:"Ubuntu",sans-serif;color:var(--text)}
.abs{position:absolute}
.top-glow{left:0;top:0;width:778px;height:214px;background:linear-gradient(#f7f7f8,#fff)}
.brand{left:74px;top:28px;display:flex;align-items:center;gap:6px;font-size:17px;font-weight:500;color:var(--red)}
.brand i{width:10px;height:10px;background:var(--navy);display:block}
.lang{left:490px;top:12px;font-size:8.5px;color:#555;display:flex;align-items:center;gap:4px}
.lang span.sel{border:1px solid #ccc;padding:3px 6px;font-size:7.5px;background:#fff}
.cart{left:624px;top:7px;font-size:10px;color:#333;display:flex;gap:3px;align-items:center}
.cart small{font-size:6.5px;color:#666}
.social{left:552px;top:42px;display:flex;gap:3px}
.social b{width:13px;height:13px;background:#4a7bbf;border-radius:2px;display:block}
.support{left:600px;top:29px;font-size:9.5px;color:var(--navy);text-align:right;width:100px;white-space:nowrap}
.phone{left:570px;top:42px;font-size:14px;line-height:17px;color:var(--red);width:130px;text-align:right;white-space:nowrap}
.nav{left:74px;top:64px;width:630px;height:32px;background:linear-gradient(#2c50b0,var(--navy-dark));display:flex}
.nav a{color:#fff;font-size:10.5px;text-decoration:none;padding:0 19px;line-height:32px;border-right:1px solid rgba(255,255,255,.25);white-space:nowrap}
.nav a:last-child{border:0}
.hero{left:74px;top:96px;width:630px;height:233px;background:#fff;border:1px solid var(--line)}
.hero-photo{left:78px;top:99px;width:620px;height:227px;background:linear-gradient(#3f6a2c 0%,#6b8f42 40%,#c9bfa6 55%,#9a9585 75%,#7fa84a 90%)}
.hero-cap{left:68px;top:250px;width:236px;height:38px;background:rgba(40,40,40,.85);color:#fff;font-size:15px;line-height:38px;padding-left:15px;white-space:nowrap}
.hero-arrows{left:664px;top:304px;color:#333;font-size:14px}
.h1{left:76px;top:354px;font-size:17px;color:#333;font-weight:400}
.copy{left:76px;top:380px;width:432px;font-size:7.6px;line-height:15px;color:var(--text);font-weight:300}
.copy p{margin-bottom:4px}
.copy strong{color:var(--navy-dark);font-weight:500}
.copy h3{font-size:8.6px;color:var(--navy-dark);font-weight:400;margin:13px 0 4px}
.side-head{left:530px;top:345px;width:173px;height:28px;background:linear-gradient(#2c50b0,var(--navy-dark));color:#fff;font-size:11px;line-height:28px;padding-left:16px;border-radius:3px 3px 0 0}
.cats{left:530px;top:373px;width:173px;border:1px solid var(--line);list-style:none}
.cats li{height:21.6px;border-bottom:1px solid var(--line);font-size:7.6px;color:var(--muted);line-height:21.6px;padding-left:18px;position:relative}
.cats li:last-child{border:0}
.cats li::after{content:"+";position:absolute;right:12px;top:5px;width:11px;height:11px;border-radius:50%;background:var(--navy-dark);color:#fff;font-size:9px;line-height:11px;text-align:center}
.secure{left:530px;top:621px;width:173px;height:93px;border:1px solid var(--line);background:#fbfbfc}
.secure .pct{position:absolute;left:16px;top:10px;font-size:24px;color:var(--red);font-weight:500}
.secure .lbl{position:absolute;left:18px;top:40px;font-size:15px;color:var(--navy-dark);line-height:18px;font-weight:500}
.secure .art{position:absolute;right:14px;top:7px;width:54px;height:80px;background:linear-gradient(#e8c35a,#b58a1e);border-radius:6px}
.why{left:530px;top:722px;width:173px;height:177px;border:1px solid var(--line)}
.why-head{height:29px;background:linear-gradient(#e52027,#c0111a);color:#fff;font-size:11px;line-height:29px;padding-left:14px;font-weight:500}
.why-photo{margin:8px 10px 0 11px;height:65px;background:linear-gradient(#f3e1c4,#e88a4a 45%,#fff4ea)}
.why h4{font-size:7.6px;color:#333;font-weight:500;margin:8px 11px 2px}
.why p{font-size:7px;color:var(--muted);line-height:12px;margin:0 11px}
.steps{left:74px;top:638px;width:435px;height:342px;background:var(--panel);border-radius:6px}
.tabs{left:86px;top:650px;width:29px}
.tab{height:47px;display:flex;align-items:center;justify-content:center;border-bottom:1px solid #ddd;font-size:11px;color:#777}
.tab span{writing-mode:vertical-rl;transform:rotate(180deg)}
.tab.on{background:var(--red);color:#fff;height:43px;border-radius:3px 0 0 3px}
.inner{left:114px;top:650px;width:382px;height:312px;background:#fff;border:1px solid #e5e5e8;border-radius:4px}
.step-no{left:137px;top:665px;width:28px;height:28px;border-radius:50%;background:var(--red);color:#fff;font-size:15px;text-align:center;line-height:28px}
.step-title{left:173px;top:665px;font-size:19px;color:#333;line-height:28px;font-weight:300}
.preview{left:406px;top:655px;width:82px;height:83px;border:1px solid #ccc;background:linear-gradient(#4d90d6,#9fd0f0 55%,#3a9a30 56%,#58b040)}
.opt{top:742px;width:154px;height:138px}
.opt1{left:140px;background:linear-gradient(135deg,#222 0%,#c8a020 50%,#111 100%)}
.opt2{left:302px;background:linear-gradient(135deg,#c21b5c 0%,#e8ecf0 50%,#3a9a3a 100%)}
.choose{top:888px;height:16px;border:1px solid #999;background:linear-gradient(#fff,#ddd);font-size:10px;line-height:14px;padding:0 5px;color:#111;white-space:nowrap}
.footer{left:0;top:1004px;width:778px;height:162px;background:var(--footer)}
.f-h{font-size:11.5px;color:#333;font-weight:400}
.f-links{font-size:7.6px;color:#555;line-height:15.5px;list-style:none}
.f-text{font-size:7.6px;color:var(--muted);line-height:15.5px;width:210px}
.vr{width:1px;background:#ddd}
.cards{left:572px;top:1051px;display:flex;gap:3px}
.cards b{width:28px;height:16px;border:1px solid #223;background:#eef;display:block}
.f-brand{left:575px;top:1094px;font-size:14px;color:#555;display:flex;align-items:center;gap:6px}
.f-brand i{width:9px;height:9px;background:#555;display:block}
.bottom{left:0;top:1166px;width:778px;height:34px;background:var(--bottom);font-size:7px;color:#555;line-height:34px;padding-left:76px}
</style>
</head>
<body>
<div class="abs top-glow"></div>
<div class="abs brand"><i></i>brimlodge.eu</div>
<div class="abs lang">Select Language <span class="sel">English ▾</span></div>
<div class="abs cart">
<svg width="14" height="12" viewBox="0 0 14 12"><path d="M0 1h3l2 7h7l2-5H4" fill="none" stroke="#222" stroke-width="1.3"/><circle cx="6" cy="10.5" r="1.2"/><circle cx="11" cy="10.5" r="1.2"/></svg>
<small>My Cart</small> 0 itmes</div>
<div class="abs social"><b></b><b></b><b></b></div>
<div class="abs support">Customer Support</div>
<div class="abs phone">0800 555 0199</div>
<nav class="abs nav"><a>Home</a><a>About Us</a><a>Our Tents</a><a>FAQ</a><a>Instrcution</a><a>Delivery &amp; Payment</a><a>Contact</a></nav>

<div class="abs hero"></div>
<div class="abs hero-photo" role="img" aria-label="Large family tent pitched on a lawn with camping chairs and a table"></div>
<div class="abs hero-cap">We Deliver Heavy Duty Tents</div>
<div class="abs hero-arrows">‹ ›</div>

<h1 class="abs h1">Pop Up Gazebos For Sale</h1>
<div class="abs copy">
<p><strong>Pop up gazebos for sale near you!</strong> We at Brimlodge have been able to expand our markets to different countries and our pop up gazebos are now available for delivery in several European countries, so your wait is over. All you have to do now is order your instant awnings from our website Brimlodge.eu Please note that we deliver to the UK, Ireland, Europe</p>
<p>Our pop up gazebos are the best on the web and are durable enough to last for years. Brimlodge offer a large range of coloured mini marquees, heavy duty gazebos and instant awnings and aims to satisfy its customers by providing them with the best quality products. All our pop up marquees are available on our website and you can order them right away!</p>
<h3>Heavy Duty Instant Awnings</h3>
<p>Our pop-up gazebos are produced with the best quality material so there is no chance of them breaking easily. The 40mm wide poles are made from the best quality, strong and durable aluminium and have strong bolts which guarantee best quality. Easy but flexible polyester has also been used in the manufacturing of our pop up gazebos with sides, together with waterproof PVC coating. Each of our instant marquees also has an 'Easy to Pop-Up and Take Down' feature which enables you to set it up and take it down whenever you want without any difficulty.</p>
<p>We also supply sandbag weights (see product descriptions for more information) and other products for our range of garden gazebos</p>
</div>

<div class="abs side-head">Product Category</div>
<ul class="abs cats">
<li>2m x 2m Brimlodge</li><li>3m x 3m Brimlodge</li><li>4m x 4m Oriental Tents</li><li>5m x 5m Oriental Tents</li><li>Clear Walls</li><li>Gutters</li><li>Parts</li><li>Roof</li><li>Sandbags</li><li>Tables</li><li>Walls</li>
</ul>
<div class="abs secure"><div class="pct">100%</div><div class="lbl">Secure<br>Shopping</div><div class="art" role="img" aria-label="Gold padlock with shopping cart illustration"></div></div>
<div class="abs why"><div class="why-head">Why Buy from Us</div><div class="why-photo" role="img" aria-label="Decorated marquee interior with dining tables"></div><h4>Suspendisse quam leo</h4><p>Molestie sed, luctus quis, feugiat in, pede. Fusce tellus. Sed metus augue, convallis et, vehicula ut, pulvinar eu, ante.</p></div>

<div class="abs steps"></div>
<div class="abs tabs">
<div class="tab on"><span>Size</span></div><div class="tab"><span>Color</span></div><div class="tab"><span>Roof</span></div><div class="tab" style="height:58px"><span>Valance</span></div><div class="tab"><span>Walls</span></div><div class="tab" style="height:58px;border:0"><span>Purchase</span></div>
</div>
<div class="abs inner"></div>
<div class="abs step-no">1</div>
<div class="abs step-title">Size</div>
<div class="abs preview" role="img" aria-label="3D preview of a white gazebo on grass"></div>
<div class="abs opt opt1" role="img" aria-label="Printed black and yellow 3m x 4.5m gazebo"></div>
<div class="abs opt opt2" role="img" aria-label="Printed pink and green 3m x 3m gazebo"></div>
<div class="abs choose" style="left:165px">Choose 3m x 4.5m</div>
<div class="abs choose" style="left:338px">Choose 3m x 3m</div>

<footer class="abs footer"></footer>
<div class="abs f-h" style="left:85px;top:1026px">Quick Links</div>
<ul class="abs f-links" style="left:86px;top:1047px"><li>Home</li><li>FAQ</li><li>Instructions</li><li>Privacy</li><li>Delivery, Payment &amp; Returns</li></ul>
<ul class="abs f-links" style="left:205px;top:1047px"><li>Terms &amp; Conditions</li><li>Support</li><li>Contact Us</li><li>Tent Templates</li></ul>
<div class="abs vr" style="left:302px;top:1028px;height:94px"></div>
<div class="abs f-h" style="left:322px;top:1026px">Brimlodge for all seasons</div>
<p class="abs f-text" style="left:323px;top:1046px">Whether for a Sales Promotion, an Exhibition, a Product Launch or Sporting Event; Recruitment, Fund raising, or just good old-fashioned selling at a County Show or other venue, our Brimlodge provide unrivalled corporate brand presence under a protective structure.</p>
<div class="abs vr" style="left:548px;top:1028px;height:94px"></div>
<div class="abs f-h" style="left:571px;top:1026px">Payment and Security</div>
<div class="abs cards"><b></b><b></b><b></b><b style="width:44px"></b></div>
<div class="abs f-brand"><i></i>brimlodge.eu</div>
<div class="abs bottom">© 2013 Company Name.&nbsp; All right reserved.&nbsp; Term of Use</div>
</body>
</html>
```